Autora necesita un cover para su nuevo libro acerca de empoderamiento femenino*

Diseño de cover para libro digital sobre empoderamiento femenino.

El título del libro es: "Las 7 Raíces del Alma Valiente"
Subtítulo: Se una mujer decidida, segura y satisfecha

Autora: Rosalba Quintero

Target Market(s)

Mujeres

Font styles to use
Sans Serif

Requirements
Must have
• El título del libro es: "Las 7 Raíces del Alma Valiente"

Autora: Rosalba Quintero
Should not have
• Sin imágenes

```html
<!DOCTYPE html>
<html lang="es">
<head>
<meta charset="utf-8">
<title>Las 7 Raíces del Alma Valiente — Rosalba Quintero</title>
<link href="https://fonts.googleapis.com/css2?family=Roboto+Condensed:wght@700;900&family=Abril+Fatface&family=Open+Sans:wght@400&family=Poppins:wght@500&display=swap" rel="stylesheet">
<style>
  :root {
    --page-bg: #e5e5e5;
    --cover-black: #050303;
    --sky-pink: #cf7f9e;
    --sky-peach: #e7a584;
    --sky-amber: #efb65e;
    --sky-dusk: #b47a34;
    --title-white: #f4f4f4;
    --title-red: #e40b0b;
    --subtitle-yellow: #e8d400;
    --author-white: #f2f2f2;
  }
  * { margin: 0; padding: 0; box-sizing: border-box; }
  html, body {
    width: 1200px; height: 800px; overflow: hidden;
    background: var(--page-bg);
  }
  .book-cover {
    position: absolute;
    left: 350px; top: 20px;
    width: 500px; height: 760px;
    background: var(--cover-black);
    overflow: hidden;
    border-radius: 3px;
  }
  .cover-photo {
    position: absolute; left: 0; top: 0;
    width: 500px; height: 400px;
    display: block;
  }
  .title-block {
    position: absolute; left: 0; top: 372px; width: 100%;
    text-align: center;
    font-family: "Roboto Condensed", "Arial Narrow", sans-serif;
    font-weight: 900;
    text-transform: uppercase;
    line-height: 67px;
    letter-spacing: -1px;
  }
  .title-line { display: block; white-space: nowrap; color: var(--title-white); font-size: 69px; }
  .title-line--lead { font-size: 75px; }
  .title-article { font-size: 36px; vertical-align: 16px; margin-right: 8px; }
  .title-number {
    font-family: "Abril Fatface", Georgia, serif;
    font-weight: 400; font-size: 92px;
    line-height: 0;
    vertical-align: -6px; margin-right: 8px;
    letter-spacing: 0;
  }
  .title-line--accent { color: var(--title-red); font-size: 70px; }
  .subtitle {
    position: absolute; left: 0; top: 596px; width: 100%;
    text-align: center;
    font-family: "Open Sans", Arial, sans-serif;
    font-size: 27px; line-height: 35px;
    color: var(--subtitle-yellow);
  }
  .author {
    position: absolute; left: 0; top: 709px; width: 100%;
    text-align: center;
    font-family: "Poppins", Arial, sans-serif;
    font-weight: 500; font-size: 30px; line-height: 36px;
    letter-spacing: 6px;
    color: var(--author-white);
  }
</style>
</head>
<body>
  <div class="book-cover">
    <svg class="cover-photo" viewBox="0 0 500 400" role="img" aria-label="Fotografía de portada: silueta de una mujer con los brazos abiertos frente a un atardecer en la playa">
      <defs>
        <linearGradient id="photo-tones" x1="0" y1="0" x2="0" y2="1">
          <stop offset="0" stop-color="var(--sky-pink)"/>
          <stop offset="0.4" stop-color="var(--sky-peach)"/>
          <stop offset="0.72" stop-color="var(--sky-amber)"/>
          <stop offset="0.88" stop-color="var(--sky-dusk)"/>
          <stop offset="1" stop-color="var(--cover-black)"/>
        </linearGradient>
      </defs>
      <rect width="500" height="400" fill="url(#photo-tones)"/>
    </svg>

    <h1 class="title-block">
      <span class="title-line title-line--lead"><span class="title-article">Las</span><span class="title-number">7</span>Raíces</span>
      <span class="title-line">Del Alma</span>
      <span class="title-line title-line--accent">Valiente</span>
    </h1>

    <p class="subtitle">Se una mujer decidida,<br>segura y satisfecha</p>

    <p class="author">Rosalba Quintero</p>
  </div>
</body>
</html>
```